Project QL quella lash

To create a stunning new business card design for "QuellaXLash" please note attached photo. Would like to see rose gold colours, black or white back ground

Target Market(s)

Women 18 to 60

Contact Information for Business Card

Modern elegant with light floral design in chrom or chrom accents

Font styles to use
Script

Requirements
Must have
• Dust rose, blush pink or rose gold colours
Nice to have
• Gold colouring or accents

```html
<!DOCTYPE html>
<html lang="en">
<head>
<meta charset="utf-8">
<title>QuellaXLash Business Cards</title>
<link href="https://fonts.googleapis.com/css2?family=Lora:wght@400;500&display=swap" rel="stylesheet">
<style>
  :root {
    --page: #ecebea;
    --card: #231f21;
    --pattern-light: #f7f7f7;
    --pattern-mid: #cfcfcf;
    --rose: #e3aac4;
    --blush: #d8a7bd;
    --white: #f3f0f1;
  }
  html, body {
    margin: 0;
    width: 1200px;
    height: 800px;
    overflow: hidden;
    background: var(--page);
    font-family: "Lora", Georgia, serif;
  }
  .card {
    position: absolute;
    left: 260px;
    width: 680px;
    height: 370px;
    background: var(--card);
    box-shadow: 0 6px 18px rgba(0,0,0,0.18);
    overflow: hidden;
  }
  .card--banded { top: 20px; }
  .card--framed { top: 410px; }

  .floral-fill {
    position: absolute;
    background: linear-gradient(135deg, var(--pattern-light) 0%, var(--pattern-mid) 50%, var(--pattern-light) 100%);
  }
  .band--top { left: 0; right: 0; top: 0; height: 58px; }
  .band--bottom { left: 0; right: 0; bottom: 0; height: 58px; }

  .frame { inset: 0; }
  .frame-inner {
    position: absolute;
    left: 30px; right: 30px; top: 30px; bottom: 30px;
    background: var(--card);
  }

  .wordmark {
    position: absolute;
    margin: 0;
    font-weight: 400;
    color: var(--rose);
    white-space: nowrap;
  }
  .card--banded .wordmark {
    top: 72px; left: 0; right: 0;
    text-align: center;
    font-size: 44px;
    padding-left: 60px;
  }
  .banded-details {
    position: absolute;
    top: 138px; left: 0; right: 0;
    padding-left: 110px;
    text-align: center;
    color: var(--white);
  }
  .banded-details .person-name {
    margin: 0 0 8px;
    font-size: 21px;
    font-weight: 400;
  }
  .banded-details p {
    margin: 0 0 6px;
    font-size: 14px;
    letter-spacing: 0.3px;
  }

  .card--framed .wordmark {
    top: 62px; left: 0; right: 0;
    text-align: center;
    font-size: 46px;
  }
  .framed-name {
    position: absolute;
    top: 146px; left: 0; right: 0;
    text-align: center;
    color: var(--blush);
  }
  .framed-name h2 {
    margin: 0;
    font-size: 22px;
    font-weight: 400;
  }
  .framed-name .role {
    margin: 2px 0 0;
    font-size: 14px;
  }
  .framed-text {
    position: absolute;
    margin: 0;
    color: var(--blush);
    font-size: 13px;
    line-height: 1.4;
  }
  .framed-email { top: 150px; right: 52px; }
  .framed-address { top: 226px; left: 300px; }
  .framed-phone { top: 286px; left: 60px; }
</style>
</head>
<body>

<section class="card card--banded" aria-label="Business card, banded layout">
  <div class="floral-fill band--top" role="img" aria-label="Black and white floral swirl pattern band"></div>
  <h1 class="wordmark">QuellaXLash</h1>
  <div class="banded-details">
    <h2 class="person-name">John Doe</h2>
    <p>+000 000 000</p>
    <p>18, Lorem ipsum dolor, sit amet, USA</p>
    <p>quellaxlash@mail.com</p>
  </div>
  <div class="floral-fill band--bottom" role="img" aria-label="Black and white floral swirl pattern band"></div>
</section>

<section class="card card--framed" aria-label="Business card, framed layout">
  <div class="floral-fill frame" role="img" aria-label="Black and white floral swirl pattern border"></div>
  <div class="frame-inner"></div>
  <h1 class="wordmark">QuellaXLash</h1>
  <div class="framed-name">
    <h2>John Doe</h2>
    <p class="role">Managing Director</p>
  </div>
  <p class="framed-text framed-email">quellaxlash@mail.com</p>
  <p class="framed-text framed-address">Lorem ipsum dolor<br>sit amet, USA</p>
  <p class="framed-text framed-phone">000 000 000</p>
</section>

</body>
</html>
```